Groundbreaking Automotive Product launch

Create a package insert for sample packs to be given away at industry trade show. The new product is an innovative automotive bumper protection system that is being introduced at a major trade show.

Fendrashield (www.fendrashield.biz) is a peel and stick clear film system that protects automobile bumpers from nicks, scratches, scrapes and scuffs. Our company is planning to sell the product to owners / operators of automated car wash businesses who will apply the product to car bumpers at the end of their normal wash cycle.

This package insert will be for sample packs that we will give away to car wash owners / operators at our trade show booth to encourage them to try the system on their own. The sample package (not for resale) includes 3 Fendrashield in a roll that is one inch in diameter and 5 inches high, one squeegee applicator (3 inch x 4 inch), and one 2 ounce bottle of spray lubricant ( 1 1/4 inch in diameter x 5 inches high). These contents will be contained in a clear plastic clamshell package. The insert is approximately 4 inches wide by 6 inches tall.

The face of the insert will not be obstructed by the package contents. it needs to contain the product logo (we will provide) and some attractive artwork showing the product in place on a car bumper - this needs to illustrate that the product is virtually invisible (except perhaps for a sparkle of sunlight off its highly polished surface) and does not change the appearance of the vehicle. The face of the insert will also require text indicating that product application helps them differentiate their car wash from the competition, is quick and easy without capital expense or staff training, can be done in a matter of seconds without disrupting the normal car wash process, preserves the appearance and resale value of the owner's vehicle, that the product is removable, the product is engineered to last up to one year, and that providing this bumper protection system can dramatically increase profits per transaction. Finally, our company contact information will also need to be included.

the back of the package insert will be obstructed partially by package contents but that does not affect insert design. the back of the insert merely needs to print application instructions (in black and white) which we will provide.
Updates

Project Deadline Extended

Target Market(s)

Owners / operators of automated car wash businesses located primarily in metropolitan areas.

Industry/Entity Type

Automotive

Requirements
Must have
• artwork must clearly indicate the product is applied to the flat surface of an automobile bumper while at the same time prominently featuring the product logo (we actually do print the logo design in one corner of the product itself).
Nice to have
• artwork that indicates the product is crystal clear and enhances the shine of the vehicle paint.
Should not have
• artwork should not suggest product is applied to bumper sections with dramatic or complex curves

```html
<!DOCTYPE html>
<html lang="en">
<head>
<meta charset="utf-8">
<title>Fendrashield – Invisible Bumper Protector insert</title>
<link href="https://fonts.googleapis.com/css2?family=Montserrat:wght@500;700;800;900&display=swap" rel="stylesheet">
<style>
  :root{
    --page:#ffffff;
    --maroon-deep:#1e0303;
    --maroon:#5a0707;
    --maroon-glow:#8a0f0f;
    --brand-red:#d0121b;
    --silver-light:#f4f4f4;
    --silver-mid:#b9bcc2;
    --silver-dark:#6d7078;
    --ribbon:#f7c229;
    --ribbon-text:#1f5fae;
    --body-ink:#1a1a1a;
    --tile-purple:#5b2a86;
    --tile-yellow:#f1c40f;
    --tile-blue:#1e63c6;
    --tile-green:#3a9a2c;
    --tile-red:#c5161d;
    --white:#ffffff;
  }
  *{box-sizing:border-box;margin:0;padding:0}
  html,body{width:1200px;height:850px;overflow:hidden;background:var(--page);font-family:"Montserrat",Arial,sans-serif}
  .insert{
    position:absolute;left:330px;top:15px;width:540px;height:820px;overflow:hidden;
    border-radius:10px;border:3px solid #111;
    background:radial-gradient(ellipse at 55% 40%,var(--maroon-glow) 0%,var(--maroon) 40%,var(--maroon-deep) 100%);
  }
  .ribbon{position:absolute;left:0;top:0;width:130px;height:130px}
  .ribbon__label{
    position:absolute;left:0;top:34px;width:100px;transform:rotate(-45deg);
    text-align:center;color:var(--ribbon-text);font-weight:900;font-size:10px;line-height:1.15;text-transform:uppercase
  }
  .brand{position:absolute;right:34px;top:42px;display:flex;align-items:center;gap:8px}
  .brand__mark{width:12px;height:12px;background:var(--brand-red)}
  .brand__name{color:var(--brand-red);font-weight:800;font-size:24px;letter-spacing:1px}
  .headline{
    position:absolute;left:0;right:0;top:118px;text-align:center;white-space:nowrap;
    font-weight:900;font-size:28px;color:var(--silver-light);
    text-shadow:0 2px 0 var(--silver-dark),0 4px 6px rgba(0,0,0,.6)
  }
  .showcase{position:absolute;left:0;top:180px;width:540px;height:380px}
  .showcase__copy{
    position:absolute;right:30px;top:212px;width:330px;text-align:right;
    font-size:10px;font-weight:700;line-height:1.3;color:var(--body-ink)
  }
  .showcase__copy p+p{margin-top:7px}
  .band{position:absolute;left:0;right:0;height:6px;
    background:linear-gradient(90deg,var(--silver-dark),var(--silver-light) 50%,var(--silver-dark))}
  .band--upper{top:600px}
  .band--lower{top:716px}
  .price{position:absolute;left:0;right:0;top:576px;text-align:center;white-space:nowrap;color:var(--white);font-weight:700;font-size:11.5px}
  .benefits{position:absolute;left:18px;right:18px;top:618px;display:flex;justify-content:space-between;list-style:none}
  .benefit{
    width:88px;height:88px;border-radius:6px;border:2px solid var(--silver-light);
    display:flex;flex-direction:column;align-items:center;justify-content:flex-end;padding:6px 4px;
    color:var(--white);font-size:9px;font-weight:700;text-align:center;line-height:1.1;box-shadow:0 3px 6px rgba(0,0,0,.5)
  }
  .benefit svg{margin-bottom:auto;margin-top:4px}
  .benefit__steps{font-size:30px;font-weight:900;margin-bottom:auto;margin-top:6px;letter-spacing:1px}
  .benefit__steps span:nth-child(2){position:relative;top:-8px}
  .benefit--purple{background:var(--tile-purple)}
  .benefit--yellow{background:var(--tile-yellow);color:var(--body-ink)}
  .benefit--blue{background:var(--tile-blue)}
  .benefit--green{background:var(--tile-green)}
  .benefit--red{background:var(--tile-red)}
  .benefit__dollar{font-size:36px;font-weight:900;margin-bottom:auto}
  .contact{position:absolute;left:0;right:0;top:734px;text-align:center;color:var(--white)}
  .contact__lead{font-size:14px;font-weight:700}
  .contact__web,.contact__phone{font-size:21px;font-weight:800;line-height:1.15}
</style>
</head>
<body>
<article class="insert">
  <svg class="ribbon" viewBox="0 0 130 130" aria-hidden="true">
    <polygon points="0,0 130,0 0,130" fill="var(--ribbon)"/>
    <polygon points="0,80 80,0 130,0 0,130" fill="#e0a416" opacity=".4"/>
  </svg>
  <div class="ribbon__label">Exclusive<br>New<br>Product</div>

  <div class="brand"><span class="brand__mark"></span><span class="brand__name">FENDRASHIELD</span></div>

  <h1 class="headline">Invisible Bumper Protector</h1>

  <svg class="showcase" viewBox="0 0 540 380" role="img" aria-label="Close-up of a glossy red car bumper with the clear protective film applied">
    <defs>
      <linearGradient id="bumperTone" x1="0" y1="0" x2="0" y2="1">
        <stop offset="0" stop-color="#c9c9cb"/>
        <stop offset=".3" stop-color="#8f8f93"/>
        <stop offset=".38" stop-color="#e5322a"/>
        <stop offset=".8" stop-color="#d8231f"/>
        <stop offset="1" stop-color="#7a0c0c"/>
      </linearGradient>
      <linearGradient id="chrome" x1="0" y1="0" x2="1" y2="1">
        <stop offset="0" stop-color="var(--silver-light)"/>
        <stop offset=".5" stop-color="var(--silver-dark)"/>
        <stop offset="1" stop-color="var(--silver-light)"/>
      </linearGradient>
    </defs>
    <ellipse cx="330" cy="190" rx="320" ry="180" fill="url(#bumperTone)"/>
    <ellipse cx="330" cy="190" rx="320" ry="180" fill="none" stroke="url(#chrome)" stroke-width="8"/>
  </svg>
  <div class="showcase__copy">
    <p>Imagine being the only car wash in the neighbourhood to offer a quick, long lasting solution to those annoying nicks and scrapes on your customers bumpers.</p>
    <p>FENDRASHIELD can be quickly applied at the end of a wash cycle. No special equipment is needed and your staff need no special training. Simply follow the three steps of application as outlined on the back of this package.</p>
  </div>

  <p class="price">Cost to you per application is only $27.45 but has a retail value of $49.99</p>
  <div class="band band--upper"></div>

  <ul class="benefits">
    <li class="benefit benefit--purple"><span class="benefit__steps"><span>1</span><span>2</span><span>3</span></span>Quick &amp; Easy Application</li>
    <li class="benefit benefit--yellow">
      <svg width="44" height="44" viewBox="0 0 44 44" aria-hidden="true"><circle cx="22" cy="22" r="18" fill="none" stroke="#111" stroke-width="4"/><line x1="9" y1="9" x2="35" y2="35" stroke="#111" stroke-width="4"/></svg>
      No Special Tools Required</li>
    <li class="benefit benefit--blue">
      <svg width="46" height="42" viewBox="0 0 46 42" aria-hidden="true"><rect x="1" y="1" width="44" height="40" fill="#fff"/><rect x="1" y="1" width="44" height="8" fill="#222"/><g stroke="#222" stroke-width="1.5"><line x1="1" y1="17" x2="45" y2="17"/><line x1="1" y1="25" x2="45" y2="25"/><line x1="1" y1="33" x2="45" y2="33"/><line x1="12" y1="9" x2="12" y2="41"/><line x1="23" y1="9" x2="23" y2="41"/><line x1="34" y1="9" x2="34" y2="41"/></g></svg>
      Lasts up to 1 Year</li>
    <li class="benefit benefit--green"><span class="benefit__dollar">$</span>High Profit Margin</li>
    <li class="benefit benefit--red">Exclusive Product</li>
  </ul>

  <div class="band band--lower"></div>

  <footer class="contact">
    <p class="contact__lead">For product and ordering information, visit</p>
    <p class="contact__web">www.fendrashield.biz</p>
    <p class="contact__phone">(743) 555-5555</p>
  </footer>
</article>
</body>
</html>
```